Company Website

We need an interactive website designed that for new company. Our company is in the Automotive fleet maintenance business. We have wide ranging customers in many industries e.g Aviation industry, construction industry, transportation etc.
We would like the website to have login accounts where customers can register, login and access their service history. Also we would like to have an appointment system where customers could schedule appointments, once appointments are made that time would no longer be available to be selected as it would be booked etc.

The website should also be updatable and provide areas for showcasing
Our services
Products/parts (possibly store front)
Customer feedback
Appointments
Our customers (where our customers can advertise or be showcased)
About us
Contacts
gallery

We would like designs that have a modern, corporate feel, One that is user friendly.
prefer a design that does not look like a template.

Target Market(s)

Medium to large companies, small business owners and the general motoring public.

Industry/Entity Type

Construction

Requirements
Must have
• Customer login set up so a database of customer vehicle maintenance history as well as the ability to schedule repairs via their account. They could also check the status of a repair.
Nice to have
• Photo gallery to show case current projects.
Our customers page where we can show case our clients they could also post their events on there, promotions etc.

The theme Should be something that's reflective of our core business; fleet maintenance. It would be nice to capture some sort of background in there that depicts some of that for example mixer trucks, tractors,loaders excavators forklifts cars trucks. That's what we deal with. It's up to the designer to capture the Essence of this as much as possible. Impress me.
Should not have
• Would prefer a custom website not a template.

```html
<!DOCTYPE html>
<html lang="en">
<head>
<meta charset="utf-8">
<title>Forefront Fleet &amp; Auto Maintenance</title>
<link href="https://fonts.googleapis.com/css2?family=Bitter:wght@400;700&family=Open+Sans:wght@400;600&display=swap" rel="stylesheet">
<style>
:root{
  --red:#d71f2b;
  --ink:#2b2b2b;
  --text:#3d3d3d;
  --muted:#6a6a6a;
  --rule:#dcdcdc;
  --card:#ececec;
  --page:#000;
  --white:#fff;
}
*{margin:0;padding:0;box-sizing:border-box}
html,body{width:1200px;height:1000px;overflow:hidden;background:var(--page)}
body{position:relative;font-family:"Open Sans",Arial,sans-serif;color:var(--text)}
.backdrop{position:absolute;left:0;top:0;width:1200px;height:580px;
  background:radial-gradient(ellipse 260px 300px at 9% 32%,#4e4e4e 0,#262626 60%,transparent 100%),
             radial-gradient(ellipse 260px 320px at 91% 34%,#505050 0,#282828 60%,transparent 100%),
             linear-gradient(#262626,#0d0d0d 75%,#000)}
.site-header{position:absolute;left:255px;top:0;width:684px;height:84px}
.brand{position:absolute;left:0;top:36px;font-family:"Bitter",serif;font-weight:700;font-size:24px;line-height:28px;color:var(--white);letter-spacing:1px;display:flex;align-items:center;gap:8px}
.brand-dot{width:13px;height:13px;background:var(--red);display:inline-block}
.utility{position:absolute;right:72px;top:19px;font-size:8px;color:#ccc;letter-spacing:.2px}
.utility span{margin:0 4px}
.register{position:absolute;right:0;top:14px;width:61px;height:23px;background:var(--red);color:var(--white);font-size:8.5px;font-weight:600;display:flex;align-items:center;justify-content:center;border-radius:2px}
.main-nav{position:absolute;right:0;top:57px;display:flex;gap:18px;font-family:"Bitter",serif;font-size:10px;font-weight:700;color:var(--white);letter-spacing:.2px;font-variant:normal;text-transform:uppercase}
.hero{position:absolute;left:255px;top:84px;width:684px;height:293px;border-bottom:3px solid var(--red);
  background:
    linear-gradient(180deg,transparent 0,transparent 58%,#5d5c58 66%,#4a4946 100%),
    linear-gradient(90deg,#b9c4c0 0,#9aa79c 25%,#e9eef0 45%,#f4f5f6 65%,#a4584a 80%,#c6c2bb 100%)}
.hero-caption{position:absolute;left:13px;top:13px}
.hero-caption span{display:inline-block;background:#111;color:var(--white);font-family:"Bitter",serif;font-weight:700;font-size:19px;line-height:25px;padding:1px 6px;margin-bottom:6px;letter-spacing:.3px}
.slider-tab{position:absolute;left:312px;bottom:0;width:60px;height:20px;background:var(--red);clip-path:polygon(8% 0,92% 0,100% 100%,0 100%);display:flex;align-items:center;justify-content:center;gap:3px}
.slider-tab i{width:8px;height:8px;border:1.5px solid #fff;border-radius:50%}
.slider-tab i.on{background:#fff}
.panel{position:absolute;left:255px;top:377px;width:684px;height:538px;background:var(--white);box-shadow:0 3px 0 #ddd,0 6px 0 #bbb,0 9px 0 #eee}
.feature{position:absolute;top:18px;width:210px}
.feature h2{font-family:"Bitter",serif;font-size:12px;font-weight:700;color:var(--red);letter-spacing:.4px;padding-bottom:7px;border-bottom:1px solid var(--rule)}
.feature-card{margin-top:26px;height:73px;background:var(--card);border:1px solid #dadada;position:relative}
.feature-card p{position:absolute;left:6px;top:6px;width:104px;font-size:8.5px;line-height:10.5px;color:#333}
.more{position:absolute;left:6px;top:45px;width:43px;height:19px;background:var(--red);color:#fff;font-size:7px;font-weight:600;display:flex;align-items:center;justify-content:center}
.feature-photo{position:absolute;right:4px;bottom:-3px;width:100px;height:90px;border-radius:3px}
.welcome{position:absolute;left:14px;top:173px;width:410px}
.welcome h2,.customers h2{font-family:"Bitter",serif;font-size:12.5px;font-weight:700;color:var(--ink);letter-spacing:.3px}
.welcome p{font-size:8.6px;line-height:12.2px;margin-top:12px}
.welcome p+p{margin-top:12px}
.welcome a{color:var(--red);text-decoration:none}
.divider{position:absolute;left:445px;top:203px;width:1px;height:142px;background:var(--rule)}
.aside{position:absolute;left:459px;top:204px;width:210px}
.appointment{height:38px;background:var(--red);color:#fff;font-family:"Bitter",serif;font-size:14.5px;display:flex;align-items:center;justify-content:center;letter-spacing:.4px}
.aside h3{margin-top:20px;font-family:"Bitter",serif;font-weight:400;font-size:11px;color:var(--ink);padding-bottom:6px;border-bottom:1px solid var(--rule);letter-spacing:.3px}
.contact-list{list-style:none;margin-top:6px;font-size:8.6px}
.contact-list li{display:flex;align-items:center;gap:5px;height:18px}
.rule{position:absolute;left:14px;top:367px;width:657px;height:1px;background:var(--rule)}
.customers{position:absolute;left:14px;top:386px;width:657px}
.customers p{font-size:8.6px;line-height:12.2px;margin-top:12px}
.client-row{position:absolute;left:54px;top:456px;display:flex;gap:14px}
.client{width:104px;height:62px;border:1px solid #d6d6d6;display:flex;align-items:center;justify-content:center;font-weight:600;font-size:12px;color:#555}
.site-footer{position:absolute;left:254px;top:950px;width:685px;font-size:8.5px;color:#b5b5b5}
.footer-nav span{margin:0 4px}
.copyright{margin-top:8px;color:#999}
.social{position:absolute;right:0;top:1px;display:flex;align-items:center;gap:4px;font-size:8.5px}
.social i{width:23px;height:23px;border-radius:50%;background:#6a6a6a;display:inline-block}
.social em{font-style:normal;margin-right:3px}
</style>
</head>
<body>
<div class="backdrop" role="img" aria-label="Dim monochrome scene of loaders, tractors and mixer trucks"></div>

<header class="site-header">
  <div class="brand"><span class="brand-dot"></span>FOREFRONT</div>
  <div class="utility">CUSTOMER FEEDBACK<span>|</span>APPOINTMENTS<span>|</span>LOGIN</div>
  <div class="register">REGISTER</div>
  <nav class="main-nav"><span>Home</span><span>About</span><span>Services</span><span>Products</span><span>Gallery</span><span>Our Customers</span><span>Contacts</span></nav>
</header>

<section class="hero" role="img" aria-label="White fleet service truck parked on a forecourt">
  <div class="hero-caption">
    <span>DUIS AUTE IRURE DOLOR IN REPREHENDERIT</span><br>
    <span>IN VOLUPTATE VELIT ESSE</span>
  </div>
  <div class="slider-tab"><i></i><i class="on"></i><i></i></div>
</section>

<main class="panel">
  <div class="feature" style="left:13px">
    <h2>OUR SERVICES</h2>
    <div class="feature-card">
      <p>Lorem ipsum dolor amet consectetur adipisicing elit sed do eiusmod.</p>
      <div class="more">MORE ›</div>
      <div class="feature-photo" role="img" aria-label="Yellow wheel loader" style="background:linear-gradient(160deg,rgba(236,236,236,0) 0,#e8b81c 40%,#c99a12 70%,#3a3a36 100%)"></div>
    </div>
  </div>
  <div class="feature" style="left:236px">
    <h2>OUR PRODUCTS</h2>
    <div class="feature-card">
      <p>Lorem ipsum dolor amet consectetur adipisicing elit sed do eiusmod.</p>
      <div class="more">MORE ›</div>
      <div class="feature-photo" role="img" aria-label="Yellow cement mixer truck" style="background:linear-gradient(180deg,#e6c21c 0,#d9b21a 45%,#8f8a78 70%,#3c3c3a 100%)"></div>
    </div>
  </div>
  <div class="feature" style="left:459px">
    <h2>OUR GALLERY</h2>
    <div class="feature-card">
      <p>Lorem ipsum dolor amet consectetur adipisicing elit sed do eiusmod.</p>
      <div class="more">MORE ›</div>
      <div class="feature-photo" role="img" aria-label="Yellow forklift" style="background:linear-gradient(180deg,rgba(236,236,236,0) 0,#565656 30%,#f0d420 55%,#e2c41a 75%,#2e2e2e 100%)"></div>
    </div>
  </div>

  <section class="welcome">
    <h2>WELCOME TO FOREFRONT</h2>
    <p>Lorem ipsum dolor sit amet consectetur adipisicing elit sed do eiusmod tempor incididunt ut labore et dolore magna aliqua. Ut enim ad minim veniam, quis nostrud exercitation ullamco laboris nisi ut commodo consequat. Duis aute irure dolor in reprehenderit in <a>voluptate velit esse cillum</a> dolore eu fugiat nulla pariatur. Excepteur sint occaecat cupidatat non proident, sunt in culpa qui officia deserunt mollit anim id est laborum.</p>
    <p>Lorem ipsum <a>dolor sit amet consectetur</a> adipisicing elit sed do eiusmod tempor incididunt ut labore et dolore magna aliqua. Ut enim ad minim veniam, quis nostrud exercitation ea commodo consequat. Duis aute irure dolor in reprehenderit in voluptate velit <a>esse cillum dolore eu</a> fugiat nulla pariatur. Excepteur sint occaecat cupidatat non proident, sunt in culpa qui officia deserunt mollit anim id est laborum. Lorem ipsum dolor sit amet consectetur adipisicing elit sed do eiusmod tempor incididunt ut labore et dolore magna aliqua.</p>
  </section>
  <div class="divider"></div>
  <aside class="aside">
    <div class="appointment">MAKE AN APPOINTMENT</div>
    <h3>QUICK CONTACT</h3>
    <ul class="contact-list">
      <li><svg width="10" height="10" viewBox="0 0 10 10"><path d="M2 0l2 2.5-1 1.2c.6 1.3 1.6 2.3 2.9 2.9l1.2-1L10 8l-1.5 2C4 10 0 6 0 1.5z" fill="#555"/></svg>555-014-2273 / 555-019-6640</li>
      <li><svg width="10" height="8" viewBox="0 0 10 8"><rect width="10" height="8" fill="#555"/><path d="M0 0l5 4 5-4" stroke="#fff" fill="none"/></svg>user@mailbox.example</li>
      <li><svg width="10" height="10" viewBox="0 0 10 10"><rect x="2" y="0" width="6" height="3" fill="#555"/><rect x="0" y="3.5" width="10" height="4" fill="#555"/><rect x="2" y="6" width="6" height="4" fill="#555" stroke="#fff" stroke-width=".8"/></svg>555-014-2273 / 555-019-6640</li>
    </ul>
  </aside>

  <div class="rule"></div>
  <section class="customers">
    <h2>OUR CUSTOMERS</h2>
    <p>Lorem ipsum dolor sit amet consectetur adipisicing elit sed do eiusmod tempor incididunt ut labore et dolore magna aliqua. Ut enim ad minim veniam, quis nostrud exercitation ullamco laboris nisi ut commodo consequat.</p>
  </section>
  <div class="client-row">
    <div class="client">KESTREL</div>
    <div class="client">ARLOW</div>
    <div class="client">NORVANE</div>
    <div class="client">TAMARO</div>
    <div class="client">CORVEL</div>
  </div>
</main>

<footer class="site-footer">
  <div class="footer-nav">Home<span>|</span>About<span>|</span>Services<span>|</span>Products<span>|</span>Gallery<span>|</span>Our Customers<span>|</span>Contacts</div>
  <div class="copyright">Copyright © 2013 Forefront. All rights reserved.</div>
  <div class="social"><em>Follow us on</em><i aria-label="Social link"></i><i aria-label="Social link"></i><i aria-label="Social link"></i><i aria-label="News feed"></i></div>
</footer>
</body>
</html>
```